Business Card Design

I am an Event and Wedding Planner in need of an eye catching business card featuring my logo (attached), my contact details, and my company tagline (Making each one of your gatherings radiant...) I would like the tagline in font similar the logo's font.
Updates
I have just noticed that my logo has a misspelling so for the final design, I will be uploading a corrected logo as soon as I have it.
My apologies.
Reason: Waiting on a corrected logo...Occasions is misspelled and it should say Weddings not Wedding
The logo has been corrected so now Occasions is spelled correctly and it says Weddings instead of Wedding. Please use Edwardian Script ITC as the font for the tagline so it will match the logo. Thank you for your patience.
Target Market(s)
Engaged couples and people hosting milestone celebrations. 25-50 years old, predominately female
Industry/Entity Type
Business
Contact Information for Business Card
Delphine Marsh, Event Manager / Owner, Mobile: 0491 836 254, Email: delphine@radiantgatheringsco.com.au, www.radiantgatheringsco.com.au, Making each one of your gatherings radiant...

```html
<!DOCTYPE html>
<html lang="en">
<head>
<meta charset="utf-8">
<title>Radiant Gatherings Co. — Business Card</title>
<link rel="stylesheet" href="https://fonts.googleapis.com/css2?family=Pinyon+Script&family=Cormorant+Garamond:ital,wght@1,500;1,700&display=swap">
<style>
  :root {
    --backdrop: #d9d9d9;
    --card: #f7fbfc;
    --ink: #141414;
    --accent: #c42127;
    --rule: #3a3a3a;
    --on-accent: #ffffff;
  }
  * { box-sizing: border-box; margin: 0; padding: 0; }
  html, body { width: 1200px; height: 840px; overflow: hidden; }
  body { background: var(--backdrop); position: relative; color: var(--ink); }

  .card {
    position: absolute;
    background: var(--card);
    box-shadow: 0 6px 18px rgba(0,0,0,.25);
    overflow: hidden;
  }

  /* Front */
  .card-front { left: 60px; top: 70px; width: 540px; height: 310px; }
  .front-brand {
    position: absolute; inset: 0;
    display: flex; align-items: center; justify-content: center; gap: 14px;
    padding: 0 48px;
  }
  .brand-name {
    font-family: "Pinyon Script", cursive;
    font-weight: 400;
    color: var(--ink);
    line-height: 1;
    white-space: nowrap;
  }
  .card-front .brand-name { font-size: 44px; }
  .brand-dot { width: 14px; height: 14px; border-radius: 50%; background: var(--accent); flex: none; }

  /* Back */
  .card-back { left: 590px; top: 400px; width: 560px; height: 320px; }
  .back-brand {
    position: absolute; left: 28px; top: 62px;
    display: flex; align-items: center; gap: 10px;
  }
  .card-back .brand-name { font-size: 32px; }
  .card-back .brand-dot { width: 10px; height: 10px; }

  .owner { position: absolute; right: 34px; top: 26px; text-align: right; }
  .owner-name {
    font-family: "Cormorant Garamond", serif;
    font-style: italic; font-weight: 700;
    font-size: 24px; letter-spacing: .3px;
  }
  .owner-title {
    font-family: "Cormorant Garamond", serif;
    font-style: italic; font-weight: 500;
    font-size: 15px; margin-top: 2px;
  }

  .contact {
    position: absolute; right: 22px; top: 102px;
    list-style: none; text-align: right;
    font-family: "Cormorant Garamond", serif;
    font-style: italic; font-weight: 700;
  }
  .contact li { display: flex; align-items: center; justify-content: flex-end; gap: 8px; height: 26px; }
  .contact .phone { font-size: 18px; font-weight: 500; letter-spacing: 1px; }
  .contact .email, .contact .web { font-size: 12.5px; }
  .icon {
    width: 22px; height: 22px; border-radius: 4px;
    background: var(--accent);
    display: inline-flex; align-items: center; justify-content: center; flex: none;
  }
  .icon svg { width: 14px; height: 14px; }

  .wave { position: absolute; left: 0; bottom: 0; width: 560px; height: 320px; }

  .tagline {
    position: absolute; left: 26px; bottom: 22px;
    font-family: "Pinyon Script", cursive;
    font-size: 22px; color: var(--on-accent);
    white-space: nowrap;
  }
</style>
</head>
<body>

  <section class="card card-front" aria-label="Business card front">
    <div class="front-brand">
      <span class="brand-name">Radiant Gatherings Co.</span>
      <span class="brand-dot"></span>
    </div>
  </section>

  <section class="card card-back" aria-label="Business card back">
    <svg class="wave" viewBox="0 0 560 320" aria-hidden="true">
      <path d="M0,236 C150,210 330,258 560,204" fill="none" stroke="var(--rule)" stroke-width="5"/>
      <path d="M0,243 C150,217 330,265 560,211 L560,320 L0,320 Z" fill="var(--accent)"/>
    </svg>

    <div class="back-brand">
      <span class="brand-name">Radiant Gatherings Co.</span>
      <span class="brand-dot"></span>
    </div>

    <div class="owner">
      <p class="owner-name">Delphine Marsh</p>
      <p class="owner-title">Event Manager / Owner</p>
    </div>

    <ul class="contact">
      <li class="phone">0491 836 254
        <span class="icon"><svg viewBox="0 0 24 24"><path fill="#fff" d="M6.6 10.8a15.1 15.1 0 0 0 6.6 6.6l2.2-2.2a1 1 0 0 1 1-.25 11.4 11.4 0 0 0 3.6.57 1 1 0 0 1 1 1V20a1 1 0 0 1-1 1A17 17 0 0 1 3 4a1 1 0 0 1 1-1h3.5a1 1 0 0 1 1 1c0 1.25.2 2.45.57 3.6a1 1 0 0 1-.25 1z"/></svg></span>
      </li>
      <li class="email">delphine@radiantgatheringsco.com.au
        <span class="icon"><svg viewBox="0 0 24 24"><circle cx="12" cy="12" r="4" fill="none" stroke="#fff" stroke-width="2"/><path d="M16 8v5a2.5 2.5 0 0 0 5 0v-1a9 9 0 1 0-3.5 7.1" fill="none" stroke="#fff" stroke-width="2"/></svg></span>
      </li>
      <li class="web">www.radiantgatheringsco.com.au
        <span class="icon"><svg viewBox="0 0 24 24" fill="none" stroke="#fff" stroke-width="1.8"><circle cx="12" cy="12" r="9"/><ellipse cx="12" cy="12" rx="4" ry="9"/><path d="M3 12h18M5 7h14M5 17h14"/></svg></span>
      </li>
    </ul>

    <p class="tagline">Making each one of your gatherings radiant...</p>
  </section>

</body>
</html>
```